Lumora Works - Design & Marketing Website Re-branding

UPDATE:
We are working on finalizing our color palette but are hoping that the designers will guide us to the right choice of colors by looking at our color inspiration file that we just uploaded and lead us in the right direction.

-----

I am exploring new design inspiration for a re-branding of my website. My current website is old and outdated and I lack the time to design it myself in addition to the fact that I am my own worst client.

I do website design, development and marketing as well as some SEO consulting and business development for small to mid-size companies in a range of industries.

https://lumoraworks.example

I like clean modern designs without cartoon images. The brands I'm going after are looking for a professional look and feel. I need something that shows my many years of being in business that is very professional.

I prefer minimal use of color. Mostly black and white with maybe one or two other colors. I am open to the suggestions by the designer.

Target Market(s)

Small to mid-size companies

Industry/Entity Type

Website Design, SEO and Markeitng

Number of Pages Required

4 page

Font styles to use
Sans Serif

Requirements
Must have
• Must be clean, modern and professional - I am not a huge fan of a lot of color and I'm open to new color suggestions by the designer
Nice to have
• A good balance of whitespace to content and graphics
Should not have
• Please no people illustrations

```html
<!DOCTYPE html>
<html lang="en">
<head>
<meta charset="utf-8">
<title>Lumora Works</title>
<link rel="stylesheet" href="https://fonts.googleapis.com/css2?family=Poppins:wght@400;500;600;700&display=swap">
<style>
:root{
  --ink:#1f1f1f;
  --paper:#f0f0f0;
  --white:#ffffff;
  --accent:#c486b6;
  --client-grey:#555555;
  --text-dark:#111111;
}
*{box-sizing:border-box;margin:0;padding:0}
html,body{width:687px;height:1200px;overflow:hidden;background:var(--ink)}
body{font-family:"Poppins",sans-serif;color:var(--white);position:relative}
.abs{position:absolute}
.btn{position:absolute;display:flex;align-items:center;justify-content:center;font-size:7.5px;border-radius:2px;color:var(--white);white-space:nowrap}
.btn-fill{background:var(--accent)}
.btn-line{border:1px solid var(--accent)}

/* hero */
.hero{position:absolute;left:0;top:0;width:687px;height:314px;background:var(--ink)}
.brand{left:51px;top:28px;font-size:12px;font-weight:700;letter-spacing:-0.2px}
.nav{left:453px;top:32px;display:flex;gap:12px;font-size:7.5px}
.headline{left:70px;top:74px;font-size:37px;font-weight:600;line-height:45.5px;letter-spacing:-0.3px;width:320px}
.lede{left:72px;top:223px;font-size:15.5px;line-height:18px;width:300px}
.showcase{left:392px;top:83px;width:222px;height:177px}
.show-head{position:absolute;left:0;top:0;width:222px;height:73px;background:var(--white);text-align:center;color:#8a2a1a}
.show-head .name{position:absolute;left:0;right:0;top:14px;font-size:13px;font-weight:700;color:#7a2416}
.show-head .tag{position:absolute;left:0;right:0;top:46px;font-size:11px;font-weight:400}
.tile{position:absolute}
.tile-label{display:flex;align-items:center;justify-content:center;font-size:9px;font-weight:500}
.dots{left:494px;top:267px;display:flex;gap:3px}
.dots span{width:3.5px;height:3.5px;border-radius:50%;background:#888}
.dots span:first-child{background:var(--white)}
.arrows{left:584px;top:262px}

/* intro */
.intro{position:absolute;left:0;top:314px;width:687px;height:348px;background:var(--paper);color:var(--text-dark)}
.intro h2{position:absolute;left:0;right:0;top:26px;text-align:center;font-size:16px;font-weight:600}
.intro .copy{position:absolute;left:106px;width:475px;top:64px;text-align:center;font-size:7.7px;line-height:11.5px}
.intro .copy p+p{margin-top:9.5px}
.pillar{position:absolute;top:173px}
.pillar h3{font-size:15.5px;font-weight:600;margin-bottom:9px;white-space:nowrap}
.pillar p{font-size:7.7px;line-height:11.4px}
.clients{position:absolute;left:0;top:288px;width:687px;height:40px}
.client{position:absolute;top:10px;width:112px;text-align:center;font-size:14px;font-weight:600;color:var(--client-grey);white-space:nowrap}

/* services */
.services{position:absolute;left:0;top:662px;width:687px;height:171px;background:var(--ink)}
.service{position:absolute;top:30px}
.service .num{font-size:32px;font-weight:400;line-height:32px;color:transparent;-webkit-text-stroke:1px var(--white)}
.service h3{font-size:15px;font-weight:600;margin-top:5px;white-space:nowrap}
.service p{font-size:7.7px;line-height:11.5px;margin-top:7px}
.service .btn{position:relative;display:inline-flex;margin-top:12px;height:21px;padding:0 9px}

/* together */
.together{position:absolute;left:0;top:833px;width:687px;height:192px}
.together .photo{position:absolute;inset:0;background:linear-gradient(135deg,#4b4a48 0%,#6b5a4c 35%,#5a4d43 60%,#3d3b3a 100%)}
.together .shade{position:absolute;inset:0;background:rgba(20,20,20,.35)}
.together h2{position:absolute;left:0;right:0;top:46px;text-align:center;font-size:16px;font-weight:600}
.together p{position:absolute;left:150px;width:387px;top:84px;text-align:center;font-size:7.7px;line-height:11.5px}

/* footer */
.footer{position:absolute;left:0;top:1025px;width:687px;height:175px;background:var(--ink)}
.footer .brand-foot{position:absolute;left:72px;top:40px;font-size:12.5px;font-weight:600;letter-spacing:-0.3px}
.social{position:absolute;left:73px;top:68px;display:flex;gap:15px}
.social span{width:9px;height:9px;border-radius:50%;background:var(--white)}
.legal{position:absolute;top:47px;font-size:7.7px}
.cta{position:absolute;left:454px;top:45px;font-size:7.7px;line-height:11.5px}
.cta strong{font-weight:600;display:block;margin-bottom:4px}
.phone{display:flex;align-items:center;gap:8px;margin-top:4px}
.copyright{position:absolute;left:0;right:0;top:146px;text-align:center;font-size:7.5px}
</style>
</head>
<body>

<header class="hero">
  <div class="abs brand">Lumora Works</div>
  <nav class="abs nav"><span>Simplify</span><span>Design</span><span>Connect</span><span>About</span></nav>
  <h1 class="abs headline">Every business has a story. We help you tell it.</h1>
  <p class="abs lede">Compelling website experiences that elevate your business.</p>
  <a class="btn btn-fill" style="left:72px;top:274px;width:57px;height:21px">Let's Chat</a>
  <a class="btn btn-line" style="left:143px;top:274px;width:57px;height:21px">What we do</a>

  <div class="abs showcase">
    <div class="show-head">
      <div class="name">Kestrel Fund</div>
      <div class="tag">We fund the future.</div>
    </div>
    <div class="tile" role="img" aria-label="Photo of a group of women" style="left:0;top:73px;width:52px;height:58px;background:linear-gradient(#6b4a36,#3a2a22)"></div>
    <div class="tile" role="img" aria-label="Portrait photo against a city backdrop" style="left:54px;top:73px;width:73px;height:58px;background:linear-gradient(#8a9aa8,#7b5a4a)"></div>
    <div class="tile" role="img" aria-label="Team group photo outdoors" style="left:129px;top:73px;width:93px;height:58px;background:linear-gradient(#6f7f6a,#3e4656)"></div>
    <div class="tile" role="img" aria-label="Food photo for Hearth Table" style="left:0;top:134px;width:72px;height:43px;background:linear-gradient(#b79a86,#3a2a4a)"></div>
    <div class="tile tile-label" style="left:75px;top:134px;width:72px;height:43px;background:#2b3360;color:#fff">Ardent Legal</div>
    <div class="tile tile-label" style="left:150px;top:134px;width:72px;height:43px;background:#eef6e0;color:#d06a2a">Tallwind</div>
  </div>
  <div class="abs dots"><span></span><span></span><span></span><span></span><span></span></div>
  <svg class="abs arrows" width="30" height="12" viewBox="0 0 30 12"><path d="M10 0 L0 6 L10 12Z" fill="#fff"/><path d="M20 0 L30 6 L20 12Z" fill="#fff"/></svg>
</header>

<section class="intro">
  <h2>We create websites that inspire</h2>
  <div class="copy">
    <p>We are a collaborative team of word nerds, choreographers of shapes &amp; ideas, ambassadors of data, content warriors and inspirational conversationalists ready to help you no matter where you are in your journey.</p>
    <p>We have a deep understanding of what it takes to grow a business and we collaborate with you every step of the way from strategy to implementation and beyond.</p>
  </div>
  <div class="pillar" style="left:73px;width:160px"><h3>Proven process</h3><p>We have carefully crafted each step in our process for successful outcomes.</p></div>
  <div class="pillar" style="left:256px;width:140px"><h3>Connection</h3><p>We take the time to truly listen and understand your audience and business needs.</p></div>
  <div class="pillar" style="left:413px;width:150px"><h3>Exceeding your goals</h3><p>We develop actionable strategies for success based on your unique goals.</p></div>
  <div class="clients">
    <span class="client" style="left:32px">Keystone</span>
    <span class="client" style="left:160px">Hearth Table</span>
    <span class="client" style="left:289px">Clickwise</span>
    <span class="client" style="left:416px">Tallwind</span>
    <span class="client" style="left:544px">Bridgepoint</span>
  </div>
</section>

<section class="services">
  <div class="service" style="left:73px;width:200px"><div class="num">1</div><h3>Websites Simplified</h3><p>A complete end-to-end website subscription solution that propels your business forward.</p><a class="btn btn-fill">Complete Website Solution</a></div>
  <div class="service" style="left:286px;width:200px"><div class="num">2</div><h3>Custom Website Design</h3><p>Blending the best principles of design, data and functionality to express your brand.</p><a class="btn btn-fill">Design Services</a></div>
  <div class="service" style="left:508px;width:145px"><div class="num">3</div><h3>Website Support</h3><p>Reliable top tier Quillsite website support, maintenance and hosting.</p><a class="btn btn-fill">Website Care</a></div>
</section>

<section class="together">
  <div class="photo" role="img" aria-label="Photo of team members stacking hands over a table"></div>
  <div class="shade"></div>
  <h2>Working with us...</h2>
  <p>Our team is well-versed in the latest web design trends and technologies, and utilize our expertise to deliver cutting-edge designs that will help your business stand out in the crowded online market.</p>
  <a class="btn btn-fill" style="left:285px;top:124px;width:117px;height:21px">Let's Work Together</a>
</section>

<footer class="footer">
  <div class="brand-foot">Lumora Works</div>
  <div class="social"><span></span><span></span><span></span><span></span></div>
  <span class="legal" style="left:241px">Privacy</span>
  <span class="legal" style="left:295px">Terms</span>
  <span class="legal" style="left:348px">Disclaimer</span>
  <div class="cta">
    <strong>Need to bounce ideas around?</strong>
    Hit us up for a quick 15-minute call and<br>let's hash it out.
    <div class="phone">
      <svg width="9" height="9" viewBox="0 0 24 24"><path fill="#fff" d="M6.6 10.8a15 15 0 0 0 6.6 6.6l2.2-2.2a1 1 0 0 1 1-.25 11.4 11.4 0 0 0 3.6.6 1 1 0 0 1 1 1V20a1 1 0 0 1-1 1A17 17 0 0 1 3 4a1 1 0 0 1 1-1h3.5a1 1 0 0 1 1 1c0 1.25.2 2.450.6 3.6a1 1 0 0 1-.25 1z"/></svg>
      <span>555-013-2847</span>
    </div>
  </div>
  <div class="copyright">© 2024 Lumora Works, LLC. All Rights Reserved.</div>
</footer>

</body>
</html>
```